Monument sign* - Law Firm

*I am installing a monument sign that has LED, as well as backlit elements. I am seeking help in designing the backlit portion of the sign. The Backlit sign will be 12’ x 4’.

We are looking for a classic, yet eye-catching sign to help new and current clients find our firm as well as bring in future clients. One of our goals is that people who drive by on a regular basis remember our sign (and us) for any future legal need.

Target Market(s)

Current and future clientele

Industry/Entity Type

Law Firm

Font styles to use
Serif
Sans Serif

Colors
b1b1b1
333333

Requirements
Must have
• Business name: Hargrove Law Firm, Inc.
• Website: www.hargrovelawfirm-example.com
• Telephone: (555)214-3679
• Our firm's logo
Nice to have
• Color preference is black, taupe, and white. A photo for reference of the office coloring is uploaded.
• We currently have an established logo which our firm has been using for more than 10 years. Our logo has been used in advertising, commercials, letterhead, and on-site. We are looking to transition from brown/rust/cream to the black/taupe/white color scheme.
Should not have
• Cheesy slogans; character designs; directions; additional symbols outside of the firm's logo.

```html
<!DOCTYPE html>
<html lang="en">
<head>
<meta charset="utf-8">
<title>Hargrove Law Firm, Inc. – Monument Sign, Option 2</title>
<link rel="stylesheet" href="https://fonts.googleapis.com/css2?family=PT+Sans:wght@400;700&family=Open+Sans:wght@400;600&family=Raleway:wght@200&display=swap">
<style>
  :root {
    --board: #f1f1f1;
    --sign-face: #353334;
    --sign-shadow: rgba(0, 0, 0, 0.28);
    --ink-light: #ffffff;
    --label-ink: #555555;
  }
  * { margin: 0; padding: 0; box-sizing: border-box; }
  html, body {
    width: 1200px;
    height: 560px;
    overflow: hidden;
    background: var(--board);
  }
  .board {
    position: relative;
    width: 1200px;
    height: 560px;
  }
  .option-label {
    position: absolute;
    left: 1076px;
    top: 28px;
    font-family: "Raleway", sans-serif;
    font-weight: 200;
    font-size: 25px;
    color: var(--label-ink);
  }
  .size-label {
    position: absolute;
    left: 120px;
    top: 92px;
    font-family: "Open Sans", sans-serif;
    font-size: 8px;
    color: #333333;
  }
  .sign {
    position: absolute;
    left: 120px;
    top: 120px;
    width: 960px;
    height: 320px;
    background: var(--sign-face);
    box-shadow: 22px 26px 22px var(--sign-shadow);
  }
  .brand {
    position: absolute;
    left: 90px;
    top: 88px;
    width: 112px;
  }
  .brand-square {
    width: 112px;
    height: 112px;
    background: var(--ink-light);
  }
  .brand-name {
    margin-top: 10px;
    font-family: "PT Sans", sans-serif;
    font-weight: 700;
    font-size: 16px;
    line-height: 20px;
    letter-spacing: 3px;
    text-align: center;
    color: var(--ink-light);
  }
  .firm-name {
    position: absolute;
    left: 253px;
    top: 82px;
    color: var(--ink-light);
  }
  .firm-name-primary {
    display: block;
    font-family: "PT Sans", sans-serif;
    font-weight: 700;
    font-size: 57px;
    line-height: 50px;
    letter-spacing: -0.5px;
  }
  .firm-name-suffix {
    display: block;
    margin-top: 6px;
    font-family: "Raleway", sans-serif;
    font-weight: 200;
    font-size: 48px;
    line-height: 50px;
  }
  .contact {
    position: absolute;
    left: 642px;
    top: 126px;
    color: var(--ink-light);
    font-family: "Open Sans", sans-serif;
  }
  .contact-phone {
    display: block;
    font-weight: 400;
    font-size: 35px;
    line-height: 42px;
  }
  .contact-web {
    display: block;
    margin-top: 2px;
    font-weight: 600;
    font-size: 16px;
    line-height: 22px;
  }
</style>
</head>
<body>
  <main class="board">
    <p class="option-label">Option 2</p>
    <p class="size-label">Size -12' x 4'</p>

    <section class="sign" aria-label="Backlit monument sign, 12 by 4 feet">
      <div class="brand">
        <div class="brand-square" aria-hidden="true"></div>
        <p class="brand-name">HARGROVE</p>
      </div>

      <h1 class="firm-name">
        <span class="firm-name-primary">HARGROVE</span>
        <span class="firm-name-primary">LAW FIRM,</span>
        <span class="firm-name-suffix">INC.</span>
      </h1>

      <p class="contact">
        <span class="contact-phone">(555)214-3679</span>
        <span class="contact-web">www.hargrovelawfirm-example.com</span>
      </p>
    </section>
  </main>
</body>
</html>
```